Biz Card for Harrowfield Property Partners - HWPP

Harrowfield Property Partners is a commercial real estate acquisitions firm. We buy commercial property and need to raise capital from investors for each deal we buy. The vibe needs to be: give us your money, we will multiply it.
Our website: www.hrwpp-example.com
Competitors are: https://velmarholdings-example.com/, https://tribanquepartners-example.com/, http://www.ostrellecapital-example.com/
Target Market(s)
High Net Worth Individuals, Bankers, Insurance Companies, Commercial Real Estate Brokers.
Industry/Entity Type
Investment Banking
Contact Information for Business Card
Name, Title, Addess, Cell#, Office#, email, website
Requirements
Must have
- use one of our logos. See website for look and feel: www.hrwpp-example.com
Nice to have
- see website: www.hrwpp-example.com

```html
<!DOCTYPE html>
<html lang="en">
<head>
<meta charset="utf-8">
<title>Harrowfield Property Partners – Business Card</title>
<link rel="stylesheet" href="https://fonts.googleapis.com/css2?family=Arimo:wght@400;700&display=swap">
<style>
  :root {
    --navy: #1b3553;
    --navy-deep: #132840;
    --ink: #1e2a38;
    --grey-band: #6d6f72;
    --paper: #ffffff;
    --paper-shade: #ecedee;
    --stage: #2e2e2f;
    --back-text: #aebfd2;
  }
  * { box-sizing: border-box; margin: 0; padding: 0; }
  html, body { width: 1200px; height: 997px; overflow: hidden; }
  body {
    background: var(--stage);
    font-family: "Arimo", Arial, sans-serif;
    position: relative;
  }
  .card {
    position: absolute;
    width: 520px;
    height: 300px;
    box-shadow: 0 18px 40px rgba(0,0,0,.55);
    overflow: hidden;
  }

  /* ---------- back of card ---------- */
  .card-back {
    left: 60px; top: 150px;
    background: linear-gradient(135deg, var(--navy) 0%, var(--navy-deep) 100%);
    color: var(--back-text);
  }
  .card-back .brand {
    position: absolute; left: 236px; top: 36px;
    display: flex; align-items: center; gap: 14px;
  }
  .card-back .brand-dot {
    width: 54px; height: 54px; border-radius: 50%;
    background: var(--paper);
    flex: none;
  }
  .card-back .brand-name {
    color: var(--paper);
    font-size: 16px; letter-spacing: 2px; line-height: 1.3;
    text-transform: uppercase; white-space: nowrap;
  }
  .offices {
    position: absolute; left: 28px; top: 98px;
    font-size: 10px; line-height: 1.35;
  }
  .office + .office { margin-top: 8px; }

  /* ---------- front of card ---------- */
  .card-front {
    left: 620px; top: 470px;
    background: linear-gradient(160deg, var(--paper) 0%, var(--paper) 55%, var(--paper-shade) 100%);
    color: var(--ink);
  }
  .card-front .brand {
    position: absolute; left: 36px; top: 34px;
    display: flex; align-items: center; gap: 16px;
  }
  .card-front .brand-dot {
    width: 82px; height: 82px; border-radius: 50%;
    background: var(--navy); flex: none;
  }
  .card-front .brand-name {
    color: var(--navy);
    font-size: 21px; letter-spacing: 2.5px; line-height: 1.3;
    text-transform: uppercase; white-space: nowrap;
  }
  .rule {
    position: absolute; height: 1px; background: var(--ink);
  }
  .rule-top { left: 134px; right: 18px; top: 124px; }
  .rule-name { left: 150px; right: 150px; top: 187px; }
  .portfolio {
    position: absolute; right: 20px; top: 130px;
    list-style: none; text-align: right;
    font-size: 11.5px; line-height: 1.3;
  }
  .portfolio .portfolio-title { font-weight: 700; }
  .person { position: absolute; left: 36px; top: 176px; }
  .person-name { font-size: 15px; }
  .person-title { font-size: 10px; }
  .contacts {
    position: absolute; left: 36px; top: 216px;
    list-style: none; font-size: 12.5px; line-height: 1;
  }
  .contacts li { display: flex; align-items: center; gap: 10px; margin-bottom: 7px; }
  .contacts svg { width: 13px; height: 13px; flex: none; }
  .card-band { position: absolute; left: 0; bottom: 0; width: 520px; height: 70px; }
  .website {
    position: absolute; right: 22px; bottom: 14px;
    color: var(--paper); font-size: 11px; font-weight: 700; letter-spacing: 1.5px;
    white-space: nowrap;
  }
</style>
</head>
<body>

<section class="card card-back" aria-label="Business card, back">
  <div class="brand">
    <span class="brand-dot"></span>
    <span class="brand-name">Harrowfield<br>Property Partners</span>
  </div>
  <div class="offices">
    <p class="office">Guatemala:<br>9 Avenida 4-20 Zona 14<br>Torre Alvora, Nivel 6, Oficina 604<br>Guatemala, C.A.<br>Phone: (502) 2555-0190</p>
    <p class="office">USA:<br>418 Marlowe Ave. Suite 310<br>Coral Gables, FL 33146<br>Phone: (786) 555-0163</p>
    <p class="office">Venezuela:<br>Av Las Palmeras, Edif Centro Orinoco, Ofc 2-B<br>Caracas 1060, Venezuela<br>Phone: (58) 212 555.01.74</p>
  </div>
</section>

<section class="card card-front" aria-label="Business card, front">
  <div class="brand">
    <span class="brand-dot"></span>
    <span class="brand-name">Harrowfield<br>Property Partners</span>
  </div>
  <div class="rule rule-top"></div>
  <ul class="portfolio">
    <li class="portfolio-title">Portfolio</li>
    <li>Office</li>
    <li>Retail</li>
    <li>Flex/other</li>
    <li>Multifamily</li>
    <li>Investments</li>
  </ul>

  <div class="person">
    <p class="person-name">Dana Whitlock</p>
    <p class="person-title">Owner</p>
  </div>
  <div class="rule rule-name"></div>

  <ul class="contacts">
    <li>
      <svg viewBox="0 0 14 14" aria-hidden="true"><circle cx="7" cy="7" r="7" fill="var(--navy)"/><path d="M4 5.5c0-1 3-1.5 3-1.5s3 .5 3 1.5l-1 .6-.6-.8H5.6l-.6.8z M5 7h4l.6 3H4.4z" fill="#fff"/></svg>
      (361) 555-0142
    </li>
    <li>
      <svg viewBox="0 0 14 14" aria-hidden="true"><circle cx="7" cy="7" r="7" fill="var(--navy)"/><rect x="4" y="6" width="6" height="3.5" fill="#fff"/><rect x="5" y="4" width="4" height="2" fill="#fff"/></svg>
      (361) 555-0187
    </li>
    <li>
      <svg viewBox="0 0 14 14" aria-hidden="true"><circle cx="7" cy="7" r="7" fill="var(--navy)"/><rect x="3.8" y="4.8" width="6.4" height="4.4" fill="none" stroke="#fff" stroke-width=".9"/><path d="M3.8 4.8 7 7.4l3.2-2.6" fill="none" stroke="#fff" stroke-width=".9"/></svg>
      info@hrwpp-example.com
    </li>
  </ul>

  <svg class="card-band" viewBox="0 0 520 70" aria-hidden="true">
    <path d="M0 56 L262 56 C280 56 284 44 288 32 C292 20 298 18 316 18 L520 18" fill="none" stroke="var(--grey-band)" stroke-width="5"/>
    <path d="M0 62 L270 62 C288 62 292 50 296 38 C300 26 306 24 324 24 L520 24 L520 70 L0 70 Z" fill="var(--navy)"/>
  </svg>
  <span class="website">www.hrwpp-example.com</span>
</section>

</body>
</html>
```